Create 5 images/buttons for our website (Casual beachfront Cafe/Restaurant)

Create 5 images/buttons to replace the "Buy a Gift Card", "Click Here to Book Now", "Download Breakfast Menu", "Download Lunch + Dinner Menu", "Download Takeaway Flyer", all currently on our website. Must be appropriately sized, compliment the existing website and brand (you can see photo of Cafe at www.saltmarrowcafe.com.au). Font and button shapes can be of your choice. Font colour should be either the red, blue or terracotta from our existing colour scheme. Thanks!

```html
<!DOCTYPE html>
<html lang="en">
<head>
<meta charset="utf-8">
<title>Salt Marrow Cafe – Website Buttons</title>
<link rel="stylesheet" href="https://fonts.googleapis.com/css2?family=Montserrat:wght@900&display=swap">
<style>
  :root {
    --blue: #174a8a;
    --terracotta: #b5561a;
    --yellow: #ffff00;
    --yellow-soft: #ffff86;
    --sand-light: #b3a199;
    --sand-dark: #a78e85;
    --egg-white: #fffbe8;
  }
  * { margin: 0; padding: 0; box-sizing: border-box; }
  html, body { width: 873px; height: 1200px; overflow: hidden; }
  body {
    position: relative;
    background: var(--sand-light);
    font-family: "Montserrat", sans-serif;
    font-weight: 900;
    color: var(--blue);
  }
  .hero-photo {
    position: absolute; left: 0; top: 0; width: 873px; height: 469px;
    background: linear-gradient(180deg, #7f8fb0 0%, #a7a3bd 28%, #4d6f9e 45%, #3a4a55 58%, #9a9686 75%, #c8c2b6 100%);
  }
  .backdrop { position: absolute; left: 0; top: 469px; width: 873px; height: 731px; }
  .button {
    position: absolute; width: 362px; height: 187px;
    border: 6px solid var(--terracotta);
    background: var(--yellow);
    overflow: hidden;
    color: inherit;
    text-decoration: none;
  }
  .button::before {
    content: ""; position: absolute; left: -40%; top: -230px;
    width: 180%; height: 300px; border-radius: 50%;
    background: var(--yellow-soft);
  }
  .button > * { position: absolute; }
  .col-left { left: 55px; }
  .col-right { left: 471px; }
  .row-1 { top: 502px; }
  .row-2 { top: 737px; }
  .row-3 { top: 972px; }
  .word { line-height: 1; white-space: nowrap; text-transform: uppercase; }
  .brand-name { left: 0; width: 100%; text-align: center; letter-spacing: -1px; }
  .art-slot { border-radius: 4px; }
  .art-blue { background: linear-gradient(180deg, #2a5c9a, var(--blue)); }
  .art-terracotta { background: linear-gradient(180deg, #c66a2c, var(--terracotta)); }
  .art-cream { background: linear-gradient(180deg, #ffffff, var(--egg-white)); }
</style>
</head>
<body>
  <div class="hero-photo" role="img" aria-label="Photo of the colourful beachfront cafe at dusk, seen across the dunes and footpath"></div>

  <svg class="backdrop" width="873" height="731" viewBox="0 0 873 731">
    <polygon points="873,0 873,731 0,731 0,564" fill="var(--sand-dark)"/>
  </svg>

  <!-- Brand tile -->
  <div class="button col-left row-1">
    <span class="word brand-name" style="top:34px;font-size:40px;">Salt Marrow</span>
    <span class="word brand-name" style="top:84px;font-size:64px;">Cafe</span>
  </div>

  <!-- Gift card -->
  <a class="button col-right row-1" href="#gift-card">
    <div class="art-slot art-blue" role="img" aria-label="Gift box illustration" style="left:20px;top:11px;width:108px;height:156px;"></div>
    <span class="word" style="left:152px;top:20px;font-size:50px;">Buy a</span>
    <span class="word" style="left:150px;top:58px;font-size:72px;letter-spacing:-2px;">Gift</span>
    <span class="word" style="left:150px;top:118px;font-size:52px;">Card</span>
  </a>

  <!-- Book now -->
  <a class="button col-left row-2" href="#book">
    <span class="word" style="left:30px;top:27px;font-size:24px;">Click here to</span>
    <span class="word" style="left:28px;top:48px;font-size:60px;letter-spacing:-2px;">Book</span>
    <span class="word" style="left:28px;top:99px;font-size:60px;letter-spacing:-2px;">Now</span>
    <svg style="left:0;top:0;" width="350" height="175" viewBox="0 0 350 175">
      <polygon points="182,112 196,112 205,140 326,8 346,8 222,170 190,172" fill="var(--blue)"/>
    </svg>
  </a>

  <!-- Breakfast menu -->
  <a class="button col-right row-2" href="#breakfast-menu">
    <svg style="left:0;top:0;" width="120" height="120" viewBox="0 0 120 120">
      <rect x="37" y="23" width="47" height="60" fill="var(--blue)"/>
      <g stroke="var(--yellow-soft)" stroke-width="2">
        <line x1="45" y1="35" x2="76" y2="35"/><line x1="45" y1="43" x2="76" y2="43"/>
        <line x1="45" y1="51" x2="76" y2="51"/><line x1="45" y1="59" x2="76" y2="59"/>
        <line x1="45" y1="67" x2="76" y2="67"/>
      </g>
      <polygon points="25,83 97,83 61,110" fill="var(--blue)"/>
    </svg>
    <div class="art-slot art-cream" role="img" aria-label="Fried egg illustration" style="left:23px;top:117px;width:80px;height:48px;"></div>
    <span class="word" style="left:134px;top:27px;font-size:27px;">Download</span>
    <span class="word" style="left:134px;top:59px;font-size:27px;">Breakfast</span>
    <span class="word" style="left:134px;top:86px;font-size:56px;">Menu</span>
  </a>

  <!-- Lunch + dinner menu -->
  <a class="button col-left row-3" href="#lunch-dinner-menu">
    <span class="word" style="left:84px;top:6px;font-size:27px;">Download</span>
    <span class="word" style="left:12px;top:51px;font-size:33px;">Lunch</span>
    <span class="word" style="left:68px;top:92px;font-size:30px;">+</span>
    <span class="word" style="left:12px;top:124px;font-size:29px;">Dinner</span>
    <div class="art-slot art-terracotta" role="img" aria-label="Serving cloche illustration" style="left:210px;top:34px;width:135px;height:84px;"></div>
    <svg style="left:0;top:0;" width="230" height="130" viewBox="0 0 230 130">
      <rect x="158" y="44" width="38" height="51" fill="var(--blue)"/>
      <g stroke="var(--yellow-soft)" stroke-width="2">
        <line x1="164" y1="54" x2="190" y2="54"/><line x1="164" y1="61" x2="190" y2="61"/>
        <line x1="164" y1="68" x2="190" y2="68"/><line x1="164" y1="75" x2="190" y2="75"/>
        <line x1="164" y1="82" x2="190" y2="82"/>
      </g>
      <polygon points="147,95 205,95 176,117" fill="var(--blue)"/>
    </svg>
    <span class="word" style="left:150px;top:120px;font-size:56px;">Menu</span>
  </a>

  <!-- Takeaway flyer -->
  <a class="button col-right row-3" href="#takeaway-flyer">
    <svg style="left:0;top:0;" width="120" height="100" viewBox="0 0 120 100">
      <rect x="45" y="15" width="40" height="55" fill="var(--blue)"/>
      <g stroke="var(--yellow-soft)" stroke-width="2">
        <line x1="51" y1="26" x2="79" y2="26"/><line x1="51" y1="34" x2="79" y2="34"/>
        <line x1="51" y1="42" x2="79" y2="42"/><line x1="51" y1="50" x2="79" y2="50"/>
        <line x1="51" y1="58" x2="79" y2="58"/>
      </g>
      <polygon points="34,70 97,70 65,95" fill="var(--blue)"/>
    </svg>
    <div class="art-slot art-blue" role="img" aria-label="Delivery scooter illustration" style="left:6px;top:102px;width:110px;height:68px;"></div>
    <span class="word" style="left:128px;top:27px;font-size:27px;">Download</span>
    <span class="word" style="left:128px;top:61px;font-size:27px;">Takeaway</span>
    <span class="word" style="left:128px;top:96px;font-size:56px;letter-spacing:-1px;">Flyer</span>
  </a>
</body>
</html>
```